I need a business card design for a new company that will be doing consulting work around issues of cultural competency, and diversity and inclusion. I would like the design to be crisp and clear with bold but conservative colors and incorporate shades of blue

Target Market(s)

Small businesses, schools, non-profits

Industry/Entity Type

Consulting

Font styles to use
Serif
Sans Serif

Colors
0c5ba6
6b449b
3276b5
0292cd

Requirements
Must have
• A Morrow Venture (name of company)
• Lemlem Tavish
• CEO
• lemlem@amorrowventure.com
• (215)483-2756

```html
<!DOCTYPE html>
<html lang="en">
<head>
<meta charset="utf-8">
<title>A Morrow Venture – Business Card</title>
<link href="https://fonts.googleapis.com/css2?family=Montserrat:wght@300;400;700&display=swap" rel="stylesheet">
<style>
  :root {
    --backdrop: #d1d2d4;
    --backdrop-edge: #6d6e70;
    --card-white: #ffffff;
    --brand-blue: #0692cd;
  }
  * { margin: 0; padding: 0; box-sizing: border-box; }
  html, body {
    width: 1200px;
    height: 1003px;
    overflow: hidden;
  }
  body {
    background: var(--backdrop);
    border: 1px solid var(--backdrop-edge);
    font-family: "Montserrat", Arial, sans-serif;
    position: relative;
  }
  .business-card {
    position: absolute;
    left: 150px;
    top: 243px;
    width: 900px;
    height: 515px;
    background: var(--card-white);
    overflow: hidden;
  }
  .card-waves {
    position: absolute;
    inset: 0;
    width: 100%;
    height: 100%;
  }
  .card-waves path { fill: var(--brand-blue); }
  .company-name {
    position: absolute;
    left: 4px;
    top: 55px;
    width: 340px;
    text-align: center;
    color: var(--card-white);
    font-weight: 700;
    font-size: 41px;
    line-height: 52px;
    letter-spacing: 1.5px;
  }
  .contact-block {
    position: absolute;
    left: 164px;
    top: 238px;
    width: 600px;
    text-align: center;
    color: var(--brand-blue);
  }
  .person-name {
    font-weight: 400;
    font-size: 57px;
    line-height: 62px;
    letter-spacing: 1.5px;
  }
  .person-title {
    font-weight: 300;
    font-size: 25px;
    line-height: 30px;
    margin-top: 4px;
  }
  .divider {
    width: 266px;
    height: 2px;
    margin: 12px auto 14px;
    background: linear-gradient(90deg, rgba(6,146,205,0) 0%, var(--brand-blue) 30%, var(--brand-blue) 70%, rgba(6,146,205,0) 100%);
  }
  .contact-line {
    display: flex;
    justify-content: center;
    align-items: center;
    gap: 12px;
    font-size: 28px;
    line-height: 43px;
    font-weight: 400;
    letter-spacing: 0.5px;
  }
  .contact-line svg {
    flex: none;
    stroke: var(--brand-blue);
    fill: none;
    stroke-width: 1.6;
    stroke-linejoin: round;
    stroke-linecap: round;
  }
  .contact-line.phone { margin-left: 10px; }
  .contact-line.email { margin-left: -20px; }
</style>
</head>
<body>
  <section class="business-card">
    <svg class="card-waves" viewBox="0 0 900 515" aria-hidden="true">
      <path d="M0 0 H292 C345 35 360 90 345 140 C325 195 270 228 200 226 C160 225 100 224 60 255 C15 290 5 350 24 388 C45 430 50 480 26 515 H0 Z"/>
      <path d="M493 0 C488 50 520 90 560 102 C600 112 640 100 665 92 C720 78 775 100 790 150 C800 185 795 220 792 240 C785 300 820 360 900 375 V0 Z"/>
    </svg>

    <h1 class="company-name">A MORROW<br>VENTURE</h1>

    <div class="contact-block">
      <h2 class="person-name">Lemlem Tavish</h2>
      <p class="person-title">(CEO)</p>
      <div class="divider"></div>
      <p class="contact-line phone">
        <svg width="28" height="28" viewBox="0 0 24 24" aria-hidden="true">
          <path d="M5 3 L8.5 3 L10 7.5 L8 9 C9 11.5 12.5 15 15 16 L16.5 14 L21 15.5 L21 19 C21 20 20 21 19 21 C10.5 20.5 3.5 13.5 3 5 C3 4 4 3 5 3 Z"/>
        </svg>
        <span>(215)483-2756</span>
      </p>
      <p class="contact-line email">
        <svg width="32" height="24" viewBox="0 0 32 24" aria-hidden="true">
          <rect x="1.5" y="2" width="29" height="20" rx="1"/>
          <path d="M1.5 2 L16 14 L30.5 2 M1.5 22 L12 11.5 M30.5 22 L20 11.5"/>
        </svg>
        <span>lemlem@amorrowventure.com</span>
      </p>
    </div>
  </section>
</body>
</html>
```